Meadowlark Learning Growth Partners (MLGP)

This is a professional business card. Logo and picture are a must on the front of the card. I am an educational consultant. I have been consulting for the past three years for a company. I am now opening my own company. My goal for my consulting company is to eventually consult all over America.

Target Market(s)

Educators, schools, professionals

Industry/Entity Type

Consulting

Contact Information for Business Card

Picture/logo on front, simple modern design

Font styles to use
Serif

Colors
85abd2
0355a3
3176b5
cedeed

Requirements
Must have
• picture, logo,
• Odessa Pruitt, Ed.S
• address 5073 Cormorant ridge Dr. Nashville, TN 37940
• Cell:616-555-0148
• Office: 629-555-0172
• www.Mlgpedu.example
• pruittodessa@mailbox.example

```html
<!DOCTYPE html>
<html lang="en">
<head>
<meta charset="utf-8">
<title>Meadowlark Learning Growth Partners – Business Card</title>
<link rel="stylesheet" href="https://fonts.googleapis.com/css2?family=Amaranth:wght@700&family=Baloo+2:wght@600;700&family=Roboto:wght@400&display=swap">
<style>
  :root {
    --page-bg: #d8d3cd;
    --card-bg: #eef0f1;
    --card-edge: #d2d6da;
    --navy: #1b3a66;
    --ink: #2a2f36;
    --photo-light: #c7cfd8;
    --photo-mid: #8e9bab;
    --photo-dark: #2c3038;
  }
  * { box-sizing: border-box; margin: 0; padding: 0; }
  html, body {
    width: 1200px;
    height: 1054px;
    overflow: hidden;
    background: var(--page-bg);
  }
  .card {
    position: absolute;
    left: 100px;
    top: 225px;
    width: 1000px;
    height: 603px;
    background: var(--card-bg);
    border: 1px solid var(--card-edge);
    border-radius: 4px;
    overflow: hidden;
    box-shadow: 0 10px 30px rgba(0,0,0,0.12);
  }
  .brand {
    position: absolute;
    left: 47px;
    top: 70px;
    height: 134px;
    display: flex;
    align-items: center;
  }
  .brand-mark {
    display: flex;
    align-items: center;
    gap: 14px;
    width: 310px;
  }
  .brand-dot {
    width: 30px;
    height: 30px;
    border-radius: 50%;
    background: var(--navy);
  }
  .brand-initials {
    font-family: "Baloo 2", sans-serif;
    font-weight: 700;
    font-size: 46px;
    letter-spacing: 3px;
    color: var(--navy);
    line-height: 1;
  }
  .brand-divider {
    width: 2px;
    height: 134px;
    background: var(--navy);
    margin-right: 20px;
  }
  .brand-name {
    font-family: "Baloo 2", sans-serif;
    font-weight: 600;
    font-size: 29px;
    line-height: 34px;
    color: var(--navy);
  }
  .person {
    position: absolute;
    left: 47px;
    top: 265px;
  }
  .person-name {
    font-family: "Amaranth", serif;
    font-weight: 700;
    font-size: 38px;
    color: var(--navy);
    line-height: 1.1;
  }
  .person-title {
    font-family: "Roboto", sans-serif;
    font-size: 22px;
    color: var(--ink);
    margin-top: 6px;
  }
  .contacts {
    position: absolute;
    left: 47px;
    top: 370px;
    list-style: none;
    font-family: "Roboto", sans-serif;
    font-size: 24px;
    color: var(--ink);
  }
  .contact-item {
    display: flex;
    align-items: center;
    height: 34px;
  }
  .contact-icon {
    width: 20px;
    height: 20px;
    margin-right: 30px;
    fill: var(--navy);
  }
  .address {
    position: absolute;
    left: 47px;
    top: 528px;
    font-family: "Roboto", sans-serif;
    font-size: 24px;
    color: var(--ink);
  }
  .portrait {
    position: absolute;
    left: 607px;
    top: 161px;
    width: 393px;
    height: 442px;
    background: linear-gradient(180deg, var(--photo-light) 0%, var(--photo-mid) 55%, var(--photo-dark) 100%);
  }
</style>
</head>
<body>
  <div class="card">
    <div class="brand">
      <div class="brand-mark">
        <span class="brand-dot"></span>
        <span class="brand-initials">MLGP</span>
      </div>
      <span class="brand-divider"></span>
      <div class="brand-name">Meadowlark<br>Learning<br>Growth<br>Partners</div>
    </div>

    <div class="person">
      <div class="person-name">Odessa Pruitt, Ed.S</div>
      <div class="person-title">Managing Director</div>
    </div>

    <ul class="contacts">
      <li class="contact-item">
        <svg class="contact-icon" viewBox="0 0 20 20" aria-hidden="true"><rect x="4" y="0" width="12" height="20" rx="2"/><rect x="6" y="3" width="8" height="12" fill="#eef0f1"/><circle cx="10" cy="17.3" r="1.2" fill="#eef0f1"/></svg>
        616-555-0148
      </li>
      <li class="contact-item">
        <svg class="contact-icon" viewBox="0 0 20 20" aria-hidden="true"><path d="M1 6c0-3 4-4 9-4s9 1 9 4v2h-4V6c-1-.6-3-1-5-1s-4 .4-5 1v2H1z"/><path d="M5 9h10l3 9H2z"/><circle cx="10" cy="13" r="2.2" fill="#eef0f1"/></svg>
        629-555-0172
      </li>
      <li class="contact-item">
        <svg class="contact-icon" viewBox="0 0 20 20" aria-hidden="true"><circle cx="10" cy="10" r="9"/><path d="M1 10h18M10 1c-3 3-3 15 0 18M10 1c3 3 3 15 0 18" stroke="#eef0f1" stroke-width="1.4" fill="none"/></svg>
        www.Mlgpedu.example
      </li>
      <li class="contact-item">
        <svg class="contact-icon" viewBox="0 0 20 20" aria-hidden="true"><rect x="0" y="3" width="20" height="14" rx="1"/><path d="M1 4l9 7 9-7" stroke="#eef0f1" stroke-width="1.6" fill="none"/></svg>
        pruittodessa@mailbox.example
      </li>
    </ul>

    <div class="address">5073 Cormorant ridge Dr. Nashville, TN 37940</div>

    <div class="portrait" role="img" aria-label="Portrait photo of Odessa Pruitt"></div>
  </div>
</body>
</html>
```